Lionel Marsbeck Card

My father, Lionel Marsbeck, just retired at 69 years old and he needs a new business/social card that looks professional and includes some sort of logo - perhaps his initials LM. It needs to include his phone number and email address and that's it. So fairly limited text but still elegant.

Industry/Entity Type

Business

```html
<!DOCTYPE html>
<html lang="en">
<head>
<meta charset="utf-8">
<title>Lionel Marsbeck – Business Card</title>
<link rel="stylesheet" href="https://fonts.googleapis.com/css2?family=Inter:wght@200;300;400&display=swap">
<style>
  :root {
    --backdrop: #e6e6e8;
    --card-slate: #58585a;
    --card-white: #ffffff;
    --name-tint: #cfcfd1;
    --contact-ink: #6a6a6c;
    --monogram-ink: #ffffff;
  }
  html, body {
    margin: 0;
    padding: 0;
    width: 1200px;
    height: 900px;
    overflow: hidden;
    background: var(--backdrop);
  }
  .stage {
    position: relative;
    width: 1200px;
    height: 900px;
  }
  .business-card {
    position: absolute;
    left: 120px;
    top: 185px;
    width: 960px;
    height: 530px;
    box-shadow: 0 10px 30px rgba(0, 0, 0, 0.12);
  }
  .business-card svg {
    display: block;
  }
  .card-band--slate { fill: var(--card-slate); }
  .card-band--white { fill: var(--card-white); }
  .monogram {
    font-family: "Inter", Helvetica, Arial, sans-serif;
    font-weight: 300;
    font-size: 290px;
    letter-spacing: -10px;
    fill: var(--monogram-ink);
  }
  .holder-name {
    font-family: "Inter", Helvetica, Arial, sans-serif;
    font-weight: 200;
    font-size: 34px;
    fill: var(--name-tint);
  }
  .contact-phone {
    font-family: "Inter", Helvetica, Arial, sans-serif;
    font-weight: 200;
    font-size: 30px;
    fill: var(--contact-ink);
  }
  .contact-email {
    font-family: "Inter", Helvetica, Arial, sans-serif;
    font-weight: 300;
    font-size: 20px;
    fill: var(--contact-ink);
  }
</style>
</head>
<body>
<main class="stage">
  <section class="business-card" aria-label="Lionel Marsbeck business card">
    <svg width="960" height="530" viewBox="0 0 960 530" xmlns="http://www.w3.org/2000/svg">
      <rect class="card-band--slate" x="0" y="0" width="960" height="414"/>
      <rect class="card-band--white" x="0" y="414" width="960" height="116"/>
      <text class="monogram" x="52" y="414">LM</text>
      <text class="holder-name" x="530" y="406">Lionel Marsbeck</text>
      <text class="contact-phone" x="690" y="482">00 0000000</text>
      <text class="contact-email" x="690" y="514">email@website.com</text>
    </svg>
  </section>
</main>
</body>
</html>
```